First Aid Training business needs business card design

We would like a double sided business card designed for a first aid training business - Brindlewood First Aid. We provide first aid training and , WHS (work, health and safety) training.

The attached word document contains the key information we would like on each side of the business card.

Final design needs to be delivered in print ready format, along with the original file.

```html
<!DOCTYPE html>
<html lang="en">
<head>
<meta charset="utf-8">
<title>Brindlewood First Aid – Business Card</title>
<link rel="stylesheet" href="https://fonts.googleapis.com/css2?family=Montserrat:wght@600;700&family=Arimo:wght@400&display=swap">
<style>
  :root {
    --page: #2a2a2a;
    --card: #0c0c0c;
    --white: #ffffff;
    --grey: #9a9a9a;
    --red: #e4202a;
    --rule: #3a3a3a;
  }
  * { margin: 0; padding: 0; box-sizing: border-box; }
  html, body { width: 1200px; height: 900px; overflow: hidden; }
  body {
    background: var(--page);
    display: flex;
    flex-direction: column;
    align-items: center;
    justify-content: center;
    gap: 44px;
  }
  .card {
    width: 640px;
    height: 366px;
    background: var(--card);
    border-radius: 22px;
    position: relative;
    overflow: hidden;
  }

  /* Front */
  .card--front .brand {
    position: absolute;
    left: 48px;
    top: 0;
    bottom: 0;
    width: 230px;
    display: flex;
    flex-direction: column;
    justify-content: center;
    align-items: flex-start;
    gap: 18px;
  }
  .brand__dot {
    width: 78px;
    height: 78px;
    border-radius: 50%;
    background: var(--red);
  }
  .brand__name {
    font-family: "Montserrat", sans-serif;
    font-weight: 700;
    color: var(--white);
    font-size: 25px;
    line-height: 1.18;
    letter-spacing: 0.04em;
    text-transform: uppercase;
  }
  .card--front .divider {
    position: absolute;
    left: 300px;
    top: 110px;
    bottom: 110px;
    width: 1px;
    background: var(--rule);
  }
  .contact {
    position: absolute;
    left: 330px;
    top: 118px;
  }
  .contact__name {
    font-family: "Montserrat", sans-serif;
    font-weight: 700;
    color: var(--red);
    font-size: 22px;
    letter-spacing: 0.03em;
    text-transform: uppercase;
    margin-bottom: 20px;
  }
  .contact__list { list-style: none; }
  .contact__item {
    display: flex;
    align-items: center;
    gap: 9px;
    font-family: "Arimo", sans-serif;
    color: var(--white);
    font-size: 14.5px;
    line-height: 1.75;
  }
  .contact__icon { width: 14px; height: 14px; flex: none; }

  /* Back */
  .card--back .brand {
    position: absolute;
    left: 0;
    right: 0;
    top: 64px;
    display: flex;
    align-items: center;
    justify-content: center;
    gap: 22px;
  }
  .card--back .brand__dot { width: 92px; height: 92px; background: var(--white); }
  .card--back .brand__name { color: var(--grey); font-size: 27px; }
  .tagline {
    position: absolute;
    left: 0;
    right: 0;
    top: 222px;
    text-align: center;
    font-family: "Arimo", sans-serif;
    font-size: 14.5px;
    line-height: 1.75;
    text-transform: none;
  }
  .tagline__lead, .tagline__services { color: var(--white); text-transform: uppercase; }
  .tagline__benefits { color: var(--red); }
</style>
</head>
<body>

  <section class="card card--front" aria-label="Business card front">
    <div class="brand">
      <div class="brand__dot" aria-hidden="true"></div>
      <p class="brand__name">Brindlewood<br>First Aid Training</p>
    </div>
    <div class="divider" aria-hidden="true"></div>
    <div class="contact">
      <p class="contact__name">Mara Ellison</p>
      <ul class="contact__list">
        <li class="contact__item">
          <svg class="contact__icon" viewBox="0 0 24 24" aria-hidden="true"><path fill="#e4202a" d="M6.6 10.8a15.1 15.1 0 0 0 6.6 6.6l2.2-2.2c.3-.3.7-.4 1-.2 1.1.4 2.3.6 3.6.6.6 0 1 .4 1 1V20c0 .6-.4 1-1 1A17 17 0 0 1 3 4c0-.6.4-1 1-1h3.5c.6 0 1 .4 1 1 0 1.3.2 2.5.6 3.6.1.3 0 .7-.2 1z"/></svg>
          0400 555 218
        </li>
        <li class="contact__item">
          <svg class="contact__icon" viewBox="0 0 24 24" aria-hidden="true"><rect x="2" y="5" width="20" height="14" rx="1.5" fill="#e4202a"/><path d="M3 6l9 7 9-7" fill="none" stroke="#0c0c0c" stroke-width="1.8"/></svg>
          help@brindlewoodfirstaid.com.au
        </li>
        <li class="contact__item">
          <svg class="contact__icon" viewBox="0 0 24 24" aria-hidden="true"><g fill="none" stroke="#e4202a" stroke-width="2"><circle cx="12" cy="12" r="9.5"/><ellipse cx="12" cy="12" rx="4" ry="9.5"/><path d="M2.5 12h19M4 7h16M4 17h16"/></g></svg>
          brindlewoodfirstaid.com.au
        </li>
      </ul>
    </div>
  </section>

  <section class="card card--back" aria-label="Business card back">
    <div class="brand">
      <div class="brand__dot" aria-hidden="true"></div>
      <p class="brand__name">Brindlewood<br>First Aid Training</p>
    </div>
    <div class="tagline">
      <p class="tagline__lead">Onsite training – we can come to you</p>
      <p class="tagline__benefits">• Time efficient &nbsp;• Cost effective &nbsp;• Minimise downtime for your team</p>
      <p class="tagline__services">First aid training &nbsp;| &nbsp;WHS training</p>
    </div>
  </section>

</body>
</html>
```